Veterinary Hospital Brochure - 2 Drafts - 1 Normal and 1 Fun.

Larchmont Pet Hospital needs a brochure to promote our veterinary hospital. These will be delivered to local mailboxes. I would like to see atleast 2 submissions from each designer.
One submission conservative and A4 folded DL and another submission more radical and interesting with innovative folding or crazy concepts. Maybe the brochure could be designed to fold into a dog house ?
I want at least one version to be VERY SIMPLE AND INTIMATE.
Our existing website is here: http://larchmontpaws.example/ and our new website will look like this: http://preview4.sitecrafto.example/#home
Please use colors and images from the new website, and information from the old website. The heading font used in the new site is Quorvatype - Marble Drift Monoline
I want the brochure to be simple and engaging on first view, and then provide the opportunity to find more information if desired. The brochure needs to be captivating on the outside so people don't throw it away immediately.

We will soon need letterhead, flags, pens, business cards, signs and vouchers so there is the opportunity for more work for the successful designer.

Target Market(s)

Women 25 to 44

Industry/Entity Type

Veterinary

Contact Information for Business Card

Larchmont Pet Hospital
14 Fenwick Grove
Tarrow Vale
NSW 2471
Phone: 02 61928357
Emergency: 0417390268
Fax: 02 84215596
www.larchmontpethospital.example
contact@larchmontpethospital.example

Font styles to use
Script

Requirements
Must have
• Colors from the new website: http://larchmontpethospital.example/ and new logo.
• Information from the old website: http://larchmontpaws.example/
• 2 drafts - A normal A4 folded DL flyer and an interesting crazy design.
Nice to have
• VERY SIMPLE
• Subdued
• Intimate
Should not have
• Intense colours
• Red

```html
<!DOCTYPE html>
<html lang="en">
<head>
<meta charset="utf-8">
<title>Larchmont Pet Hospital – Brochure</title>
<link rel="stylesheet" href="https://fonts.googleapis.com/css2?family=Montserrat:ital,wght@0,400;0,500;0,700;0,800;1,400;1,600;1,700;1,800&display=swap">
<style>
  :root {
    --orange: #f48d50;
    --green: #8aa65c;
    --charcoal: #47423f;
    --cream: #fdf6f2;
    --ink: #3a3533;
    --brown: #4a3427;
    --white: #ffffff;
  }
  html, body { margin: 0; padding: 0; overflow: hidden; background: #e9e6e3; }
  .canvas {
    position: relative; width: 1200px; height: 848px; overflow: hidden;
    background: var(--cream);
    font-family: "Montserrat", Arial, sans-serif; color: var(--ink);
  }
  .photo { position: absolute; top: 0; }
  .photo--cat {
    left: 400px; width: 400px; height: 572px;
    background: radial-gradient(ellipse at 55% 35%, #5b4b3f 0%, #3d3532 55%, #2e2927 100%);
  }
  .photo--owner {
    left: 800px; width: 400px; height: 554px;
    background: linear-gradient(180deg, #a4d6c9 0%, #c9d8c2 40%, #d8c9a8 70%, #7a6450 100%);
  }
  .bands { position: absolute; left: 0; top: 0; width: 1200px; height: 848px; pointer-events: none; }

  /* Inside left panel */
  .mission {
    position: absolute; left: 0; top: 0; width: 400px; height: 102px; margin: 0;
    background: var(--charcoal); color: var(--white);
    font-size: 15px; line-height: 20px; text-align: center;
    box-sizing: border-box; padding: 11px 10px 0;
  }
  .section-title {
    position: absolute; left: 0; width: 400px; margin: 0; text-align: center;
    color: var(--green); font-weight: 700; text-decoration: underline;
    text-decoration-thickness: 2px; text-underline-offset: 4px;
  }
  .section-title--goals { top: 113px; font-size: 21px; line-height: 26px; }
  .section-title--services { top: 271px; font-size: 40px; line-height: 48px; text-decoration-thickness: 3px; }
  .goals {
    position: absolute; left: 15px; top: 157px; width: 380px; margin: 0; padding: 0;
    list-style: none; font-size: 16.5px; line-height: 22.6px;
  }
  .goals li, .services li { position: relative; padding-left: 20px; }
  .goals li::before {
    content: ""; position: absolute; left: 0; top: 6px; width: 10px; height: 10px; background: var(--orange);
  }
  .services {
    position: absolute; top: 332px; margin: 0; padding: 0; list-style: none;
    font-size: 13.5px; line-height: 15.5px;
  }
  .services li { margin-bottom: 7.2px; padding-left: 17px; }
  .services li::before {
    content: ""; position: absolute; left: 0; top: 4px; width: 8px; height: 8px; background: var(--orange);
  }
  .services--first { left: 28px; width: 192px; }
  .services--second { left: 222px; width: 176px; }

  /* Contact panel */
  .contact { position: absolute; left: 400px; top: 638px; width: 400px; text-align: center; }
  .contact__name {
    margin: 0 0 10px; font-size: 28px; font-weight: 700; font-style: italic; color: var(--ink);
    text-decoration: underline; text-decoration-thickness: 2px; text-underline-offset: 4px;
  }
  .contact__lines { margin: 0; font-style: italic; font-size: 16px; line-height: 20.5px; color: var(--ink); }

  /* Cover panel */
  .wordmark {
    position: absolute; left: 800px; top: 168px; width: 400px; text-align: center;
    font-weight: 700; color: var(--brown); font-size: 30px; line-height: 36px; letter-spacing: 1px;
  }
  .cover-title {
    position: absolute; left: 800px; top: 626px; width: 400px; margin: 0; text-align: center;
    color: var(--white); font-weight: 800; font-style: italic; line-height: 1;
    text-shadow: 2px 2px 0 rgba(70,50,40,0.35);
  }
  .cover-title__line1 { display: block; font-size: 47px; }
  .cover-title__line2 { display: block; font-size: 38px; margin-top: 6px; }
  .cover-rule { position: absolute; left: 835px; top: 738px; width: 328px; height: 2px; background: var(--white); }
  .cover-tagline {
    position: absolute; left: 802px; top: 751px; width: 396px; margin: 0; text-align: center;
    color: var(--white); font-size: 11.8px; line-height: 17.5px; font-weight: 700; font-style: italic;
  }
</style>
</head>
<body>
<main class="canvas">
  <div class="photo photo--cat" role="img" aria-label="Photo of a cat lying on its side looking at the camera, under a dark tint"></div>
  <div class="photo photo--owner" role="img" aria-label="Photo of a young woman hugging her dog against a soft sky"></div>

  <svg class="bands" viewBox="0 0 1300 919" preserveAspectRatio="none" aria-hidden="true">
    <polygon fill="var(--green)" points="0,612 210,690 378,603 345,628 210,718 0,648"/>
    <polygon fill="var(--charcoal)" points="0,655 210,738 433,588 433,620 210,768 0,692"/>
    <polygon fill="var(--orange)" points="0,705 210,782 433,634 433,919 0,919"/>
    <polygon fill="var(--charcoal)" points="205,778 170,796 230,770"/>
    <polygon fill="var(--charcoal)" points="433,585 655,450 867,508 867,562 655,488 433,622"/>
    <polygon fill="var(--cream)" points="433,622 655,488 867,562 867,919 433,919"/>
    <polygon fill="var(--green)" points="490,606 655,500 867,560 867,602 655,537 500,612"/>
    <polygon fill="var(--green)" points="867,470 1075,550 1258,465 1232,498 1075,585 867,510"/>
    <polygon fill="var(--charcoal)" points="867,512 1075,592 1300,494 1300,540 1060,640 867,565"/>
    <polygon fill="var(--orange)" points="867,580 1060,652 1300,548 1300,919 867,919"/>
    <polygon fill="var(--charcoal)" points="1060,640 1050,660 1100,622"/>
  </svg>

  <!-- Inside left panel -->
  <p class="mission">Larchmont Pet Hospital is a Companion Animal Veterinary Hospital in Tarrow Vale committed to providing excellent care for loved pets and their owners.</p>

  <h2 class="section-title section-title--goals">To Achieve This We:</h2>
  <ul class="goals">
    <li>Provide a welcoming environment.</li>
    <li>Treat all patients and owners as important.</li>
    <li>Educate owners to help prevent illness.</li>
    <li>When illness occurs, treat with the latest equipment and techniques.</li>
  </ul>

  <h2 class="section-title section-title--services">Services</h2>
  <ul class="services services--first">
    <li>Puppy Pre-School</li>
    <li>Vaccinations</li>
    <li>Vaccination Reminders</li>
    <li>Companion Animal<br>De-sexing</li>
    <li>Emergency Surgery</li>
    <li>Dental</li>
    <li>Caeserian</li>
    <li>Behaviour Consults</li>
    <li>Grieving Support</li>
  </ul>
  <ul class="services services--second">
    <li>Aged Care Consults</li>
    <li>Nutrition Advice</li>
    <li>Flea Treatments</li>
    <li>Radiology</li>
    <li>Ultrasound</li>
    <li>Routine Blood Tests</li>
    <li>Orthopaedic Surgery</li>
    <li>Cruiciate Repair</li>
    <li>Skin Treatments</li>
  </ul>

  <!-- Contact panel -->
  <section class="contact">
    <h2 class="contact__name">Larchmont Pet Hospital</h2>
    <p class="contact__lines">
      14 Fenwick Grove, Tarrow Vale, NSW 2471<br>
      Phone: 02 61928357 &nbsp;|&nbsp; Fax : 02 84215596<br>
      Email: contact@larchmontpethospital.example<br>
      www.larchmontpethospital.example
    </p>
  </section>

  <!-- Cover panel -->
  <div class="wordmark">LARCHMONT PET<br>HOSPITAL</div>
  <h1 class="cover-title">
    <span class="cover-title__line1">LARCHMONT</span>
    <span class="cover-title__line2">PET HOSPITAL</span>
  </h1>
  <div class="cover-rule"></div>
  <p class="cover-tagline">Larchmont Pet Hospital is a Companion Animal<br>Veterinary Hospital in Tarrow Vale committed to<br>providing excellent care for loved pets and their owners.</p>
</main>
</body>
</html>
```